Multi-Faceted Legal and Finanacial Advisory Group Needs Business Card Design

We need a business card design for a newly branded Orlando Florida area advising group consisting of Attorneys, Accountants and Financial Planners. The company is named TK Counsel Partners. You will find our initial work on a business card. The information on the business card are merely guideposts and not final product. The logo does not have the be the same as provided since we have not finalized the logo. We would like to stay with a black/white/grey color scheme, but limited use of color is not out of the question.

Target Market(s)

Businesses and their Corporate Representatives

Industry/Entity Type

Business

Contact Information for Business Card

Should have Name, Title, Phone, Cell, Fax, Email and website. Logo should incorporate TK in some fashion however final logo used does not have to be the one on the document provided.

Requirements
Must have
• An TK design on front and back.

```html
<!DOCTYPE html>
<html lang="en">
<head>
<meta charset="utf-8">
<title>TK Counsel Partners – Business Card</title>
<link rel="stylesheet" href="https://fonts.googleapis.com/css2?family=Copse&family=Open+Sans:ital,wght@1,300&display=swap">
<style>
  :root {
    --graphite-glow: #4b4e55;
    --graphite-mid: #26282d;
    --graphite-deep: #0a0b0d;
    --text-white: #ffffff;
    --text-soft: #eeeff2;
    --mark-silver: #cfd1d6;
  }
  html, body {
    margin: 0;
    padding: 0;
    overflow: hidden;
    background: #ffffff;
  }
  .card {
    position: relative;
    width: 1200px;
    height: 702px;
    overflow: hidden;
    background: radial-gradient(ellipse 70% 75% at 52% 36%, var(--graphite-glow) 0%, var(--graphite-mid) 48%, var(--graphite-deep) 100%);
  }
  .holder-name {
    position: absolute;
    left: 61px;
    top: 66px;
    margin: 0;
    font-family: "Copse", serif;
    font-weight: 400;
    font-size: 54px;
    line-height: 1.1;
    letter-spacing: 1.5px;
    color: var(--text-white);
    text-shadow: 0 2px 4px rgba(0, 0, 0, 0.6);
  }
  .contact-lines {
    position: absolute;
    left: 61px;
    top: 136px;
    margin: 0;
    padding: 0;
    list-style: none;
    font-family: "Open Sans", sans-serif;
    font-style: italic;
    font-weight: 300;
    font-size: 39px;
    line-height: 52px;
    letter-spacing: 0.4px;
    color: var(--text-soft);
    white-space: nowrap;
  }
  .brand-mark {
    position: absolute;
    left: 713px;
    top: 155px;
    width: 404px;
    height: 349px;
    display: flex;
    align-items: center;
    justify-content: center;
    font-family: "Copse", serif;
    font-size: 210px;
    line-height: 1;
    color: var(--mark-silver);
  }
</style>
</head>
<body>
  <main class="card">
    <h1 class="holder-name">Thomas K. XXXXXX</h1>
    <ul class="contact-lines">
      <li class="title">Attorney</li>
      <li class="street">1620 Meridian Parkway,</li>
      <li class="suite">Suite 2045,</li>
      <li class="city">Lake Mary, FL 32746</li>
      <li class="office">Off: (407) XXX-XXXX</li>
      <li class="cell">Cell: (407) XXX-XXXX</li>
      <li class="fax">Fax: (407) XXX-XXXX</li>
      <li class="email">Email: XXXX@tk-counsel.com</li>
      <li class="web">Web: www.tk-counsel.com</li>
    </ul>
    <div class="brand-mark" aria-label="TK Counsel Partners">TK</div>
  </main>
</body>
</html>
```